Home page in PSD needed for a Business Consultant website

We have been given the mandate to re-do the website: http://www.lumivanconseil.ca/

Deliverable: home page in PSD format in French language

Context: Luc Dorval is a business strategist specializing in marketing, creativity, business development. He helps small and medium companies develop their business through creative marketing strategies.

Some websites we like for your inspiration:

http://www.tallpinegrove.com.au/
http://www.trwadvisory.com.au/
http://fjalladvisors.com.au/
http://www.olubrenix.com/fr

Target Market(s)

B2B: Companies looking on the web for a business consultant who can help them with marketing, business developement, printing needs.

Industry/Entity Type

Business

Requirements
Must have
• Call to action: "Simplifiez votre développement des affaires" (which means "Simplify your business development")
• List of services (main menu)
• Marketing
• Développement des affaires
• Créativité
• Scolaire
• Impression
• Top menu as follow:
• Accueil
• À propos
• Contact

```html
<!DOCTYPE html>
<html lang="fr">
<head>
<meta charset="utf-8">
<title>Lumivan Conseil — Accueil</title>
<link href="https://fonts.googleapis.com/css2?family=Roboto+Condensed:wght@300;400;700&display=swap" rel="stylesheet">
<style>
:root{
  --blue:#1a82cf;
  --blue-dark:#0f67ad;
  --hero-top:#2a8ad2;
  --hero-bottom:#0c68b4;
  --heading-blue:#1878c4;
  --navy:#05305a;
  --ink:#4a4a4a;
  --muted:#6b6b6b;
  --grey-btn:#4b4b4b;
  --input:#d7e9f7;
  --page:#fafafa;
  --line:#dcdcdc;
  --black:#0d0d0d;
}
*{box-sizing:border-box;margin:0;padding:0}
html,body{width:1200px;height:2256px;overflow:hidden}
body{position:relative;background:var(--page);font-family:"Roboto Condensed",Arial,sans-serif;color:var(--ink)}
.abs{position:absolute}

/* header */
.site-header{position:absolute;left:0;top:0;width:1200px;height:170px;background:#fff}
.brand{left:110px;top:22px}
.brand-name{font-size:44px;font-weight:400;color:#2b2b2b;letter-spacing:1px;line-height:1}
.brand-tag{font-size:13px;color:var(--blue-dark);margin-top:8px;letter-spacing:1px}
.header-phone{left:740px;top:42px;display:flex;align-items:center;gap:10px;font-size:15px;font-weight:700;color:var(--blue-dark)}
.top-menu{left:915px;top:44px;font-size:13px;color:var(--muted);display:flex;gap:14px;white-space:nowrap}
.top-menu span.sep{color:#bbb}
.main-nav{left:110px;top:112px;display:flex;height:42px;align-items:center;font-size:13px;color:#333;white-space:nowrap}
.main-nav a{text-decoration:none;color:#333;padding:0 16px;line-height:42px;height:42px}
.main-nav a.active{background:var(--blue);color:#fff;padding:0 20px}
.lang-select{left:950px;top:116px;width:140px;height:32px;background:#e4e4e4;border:1px solid #d0d0d0;font-size:11px;color:#666;padding:8px 6px}
.lang-select::after{content:"";position:absolute;right:10px;top:13px;border:6px solid transparent;border-top-color:#888}

/* hero */
.hero{left:0;top:170px;width:1200px;height:446px;background:linear-gradient(180deg,var(--hero-top),var(--hero-bottom))}
.hero-band{left:0;top:616px;width:1200px;height:116px;background:linear-gradient(180deg,#e6e6e6,var(--page))}
.hero-person{left:170px;top:193px;width:138px;height:535px;border-radius:60px 60px 10px 10px;background:linear-gradient(180deg,#3a3f4c,#1b1e27)}
.hero-title{left:670px;top:262px;width:480px;font-size:26px;line-height:32px;font-weight:700;color:#fff}
.hero-text{left:674px;top:350px;width:356px;font-size:14px;line-height:22px;color:#fff}
.btn-dark{background:var(--grey-btn);color:#fff;font-size:12px;text-align:center;border-radius:2px}
.hero-btn{left:672px;top:512px;width:90px;height:29px;line-height:29px}
.slider-dots{left:1006px;top:658px;display:flex;gap:6px}
.slider-dots i{width:15px;height:15px;border-radius:50%;background:var(--blue)}
.slider-dots i:first-child{background:#333}

/* mission */
.mission{left:0;top:800px;width:1200px;text-align:center;font-size:31px;font-weight:300;color:#6a6a6a;line-height:36px}

/* services */
.service{top:945px;width:277px}
.service h3{font-size:19px;font-weight:700;color:var(--heading-blue);margin-bottom:18px;white-space:nowrap}
.service-img{width:277px;height:183px;border:1px solid var(--line);background:#fff;padding:6px}
.service-img div{width:100%;height:100%}
.service p{margin-top:36px;font-size:13px;line-height:19px;color:var(--muted);text-align:justify}
.btn-blue{background:var(--blue);color:#fff;font-size:12px;text-align:center;border-radius:2px}
.service .btn-blue{width:92px;height:29px;line-height:29px;margin:29px auto 0}

.divider{left:0;top:1362px;width:1200px;height:8px;background:#e6e6e6}

/* about */
.about{left:110px;top:1410px;width:448px}
.about h3{font-size:19px;font-weight:700;color:var(--heading-blue);margin-bottom:12px}
.about p{font-size:13px;line-height:19px;color:var(--muted);text-align:justify}
.about-btn{left:110px;top:1681px;width:90px;height:29px;line-height:29px}

/* news */
.news{left:611px;top:1414px;width:479px;height:298px;background:#fff;border:1px solid var(--line)}
.news-tabs{height:35px;background:var(--blue-dark);display:flex;align-items:center;font-size:14px;color:#fff}
.news-tabs span{padding:0 16px}
.news-tabs span.active{color:#bfe0ff}
.news-item{position:absolute;left:18px;display:flex;gap:16px}
.date{width:83px;height:92px;background:#ececec;text-align:center;color:#444}
.date b{display:block;font-size:22px;padding-top:22px}
.date small{font-size:12px}
.news-item h4{font-size:16px;font-weight:400;color:#333;margin:8px 0 10px}
.news-item p{width:345px;font-size:12px;line-height:19px;color:var(--muted)}
.view-all{position:absolute;right:18px;bottom:20px;font-size:13px;color:var(--blue);text-decoration:underline}

/* footer */
.site-footer{left:0;top:1795px;width:1200px;height:426px;background:var(--navy)}
.footer-bar{left:0;top:2221px;width:1200px;height:35px;background:var(--black);color:#eee;font-size:13px;text-align:center;line-height:35px}
.footer-h{font-size:19px;font-weight:700;color:#fff}
.field{background:var(--input);font-size:13px;color:#666;padding:0 12px;line-height:39px;height:39px}
.submit{left:233px;top:2109px;width:233px;height:41px;line-height:41px;font-size:14px;border-radius:3px}
.touch{font-size:15px;color:#fff;display:flex;align-items:center;gap:14px}
.social-label{left:630px;top:2116px;font-size:19px;font-weight:700;color:var(--blue)}
.social{left:822px;top:2111px;display:flex;gap:11px}
.social i{width:34px;height:34px;border-radius:50%;background:#fff}
</style>
</head>
<body>

<header class="site-header">
  <div class="abs brand">
    <div class="brand-name">Lumivan Conseil</div>
    <div class="brand-tag">commercialisation | marketing | créativité</div>
  </div>
  <div class="abs header-phone">
    <svg width="18" height="16" viewBox="0 0 18 16"><path d="M2 5c0-3 3-4 7-4s7 1 7 4l-3 1-1-2H6L5 6z M4 8h10l2 7H2z" fill="#222"/></svg>
    514-555-0182
  </div>
  <div class="abs top-menu"><span>ACCUEIL</span><span class="sep">|</span><span>À PROPOS</span><span class="sep">|</span><span>CONTACT</span></div>
  <nav class="abs main-nav">
    <a class="active">ACCUEIL</a><a>MARKETING</a><a>DÉVELOPPEMENT DES AFFAIRES</a><a>CRÉATIVITÉ</a><a>SCOLAIRE</a><a>IMPRESSION</a><a>CONTACT</a>
  </nav>
  <div class="abs lang-select">LANGUE</div>
</header>

<section>
  <div class="abs hero"></div>
  <div class="abs hero-band"></div>
  <div class="abs hero-person" role="img" aria-label="Photo d'un consultant en complet foncé, debout"></div>
  <h1 class="abs hero-title">SIMPLIFIEZ VOTRE DÉVELOPPEMENT<br>DES AFFAIRES</h1>
  <p class="abs hero-text">Lorem Ipsum is simply dummy text of the printing and typesetting industry. Lorem Ipsum has been the industry's standard dummy text ever since the 1500s, when an unknown printer took a galley of type and scrambled it to make a type specimen book. It has survived not only five</p>
  <div class="abs btn-dark hero-btn">Lire la suite</div>
  <div class="abs slider-dots"><i></i><i></i><i></i><i></i></div>
</section>

<p class="abs mission">Aider les entreprises avant-gardistes à atteindre leur plein potentiel grâce à<br>des services-conseils de grande qualité et à prix abordable</p>

<section>
  <article class="abs service" style="left:110px">
    <h3>MARKETING</h3>
    <div class="service-img"><div role="img" aria-label="Photo d'une équipe en réunion autour d'un portable" style="background:linear-gradient(135deg,#c9b7a8,#6f7d8f)"></div></div>
    <p>Lorem Ipsum is simply dummy text of the printing and typesetting industry. Lorem Ipsum has been the industry's standard dummy text ever since the 1500s,</p>
    <div class="btn-blue">LIRE LA SUITE</div>
  </article>
  <article class="abs service" style="left:462px">
    <h3>DÉVELOPPEMENT DES AFFAIRES</h3>
    <div class="service-img"><div role="img" aria-label="Photo de mains révisant des documents avec un stylo" style="background:linear-gradient(135deg,#eef0f2,#b9bdc4)"></div></div>
    <p>Lorem Ipsum is simply dummy text of the printing and typesetting industry. Lorem Ipsum has been the industry's standard dummy text ever since the 1500s,</p>
    <div class="btn-blue">LIRE LA SUITE</div>
  </article>
  <article class="abs service" style="left:815px">
    <h3>CRÉATIVITÉ</h3>
    <div class="service-img"><div role="img" aria-label="Illustration de personnages assemblant de grandes pièces de casse-tête" style="background:linear-gradient(135deg,#f2f2f2,#cfd3d8)"></div></div>
    <p>Lorem Ipsum is simply dummy text of the printing and typesetting industry. Lorem Ipsum has been the industry's standard dummy text ever since the 1500s,</p>
    <div class="btn-blue">LIRE LA SUITE</div>
  </article>
</section>

<div class="abs divider"></div>

<section class="abs about">
  <h3>À PROPOS</h3>
  <p>Lorem Ipsum is simply dummy text of the printing and typesetting industry. Lorem Ipsum has been the industry's standard dummy text ever since the 1500s, when an unknown printer took a galley of type and scrambled it to make a type specimen book. It has survived not only five centuries, but also the leap into electronic typesetting, remaining essentially unchanged. It was popularised in the 1960s with the release of Letraset sheets containing Lorem Ipsum passages, and more recently with desktop publ sheets containing Lorem Ipsum passages, and more recently with desktop publishing software like Aldus PageMaker including versions of Lorem Ipsum.</p>
</section>
<div class="abs btn-dark about-btn">LIRE LA SUITE</div>

<section class="abs news">
  <div class="news-tabs"><span class="active">Nouvelles .</span><span>Événements .</span><span>Témoignages .</span></div>
  <div class="news-item" style="top:46px">
    <div class="date"><b>SEPT</b><small>28-2013</small></div>
    <div><h4>Titre de la nouvelle ici</h4><p>Lorem Ipsum is simply dummy text of the printing and typesetting industry. Lorem Ipsum has been the industry's standard dummy</p></div>
  </div>
  <div class="news-item" style="top:156px">
    <div class="date"><b>SEPT</b><small>28-2013</small></div>
    <div><h4>Titre de la nouvelle ici</h4><p>Lorem Ipsum is simply dummy text of the printing and typesetting industry. Lorem Ipsum has been the industry's standard dummy</p></div>
  </div>
  <span class="view-all">Voir tout</span>
</section>

<footer>
  <div class="abs site-footer"></div>
  <h3 class="abs footer-h" style="left:110px;top:1833px">NOUS JOINDRE</h3>
  <div class="abs field" style="left:110px;top:1891px;width:233px">Votre nom</div>
  <div class="abs field" style="left:354px;top:1891px;width:235px">Adresse courriel</div>
  <div class="abs field" style="left:110px;top:1941px;width:233px">Téléphone</div>
  <div class="abs field" style="left:354px;top:1941px;width:235px">Nom de l'entreprise</div>
  <div class="abs field" style="left:110px;top:1993px;width:479px;height:103px">Message</div>
  <div class="abs btn-blue submit">ENVOYER VOTRE MESSAGE</div>

  <h3 class="abs footer-h" style="left:630px;top:1833px">RESTONS EN CONTACT</h3>
  <div class="abs touch" style="left:630px;top:1893px">
    <svg width="26" height="30" viewBox="0 0 26 30"><path d="M5 2l6 6-3 4c2 4 5 7 9 9l4-3 5 6-4 4C12 27 2 17 1 6z" fill="#2c9be6"/></svg>
    514-555-0182
  </div>
  <div class="abs touch" style="left:863px;top:1897px">
    <svg width="30" height="20" viewBox="0 0 30 20"><rect width="30" height="20" fill="#2c9be6"/><path d="M0 0l15 11L30 0" stroke="#05305a" stroke-width="2" fill="none"/></svg>
    info@lumivan.ca
  </div>
  <div class="abs touch" style="left:630px;top:1955px;align-items:flex-start">
    <svg width="26" height="34" viewBox="0 0 26 34"><path d="M13 1C6 1 1 6 1 13c0 9 12 20 12 20s12-11 12-20C25 6 20 1 13 1z" fill="#2c9be6"/><circle cx="13" cy="13" r="5" fill="#05305a"/></svg>
    <div style="line-height:22px">ADRESSE POSTALE&nbsp; :<br>L'adresse postale va ici..</div>
  </div>
  <div class="abs social-label">RÉSEAUX SOCIAUX :</div>
  <div class="abs social"><i></i><i></i><i></i><i></i></div>

  <div class="abs footer-bar">2013 Tous droits réservés par lumivanconseil.ca</div>
</footer>

</body>
</html>
```